Business card design - landscaping industry

Hello! We are very creative when it comes to landscape design but when it comes to designing business cards - not so much. We could use some help to come up with a design which is professional but fun. We are based in Grand Rapids, MI and work with high end properties for new landscape design and install. We are looking to have a template made for business card for a couple of us on staff.

You can get the flavor of our color scheme from our attached logo. We probably would want to highlight the green but also include some of the blue maybe.

Target Market(s)

We work with residential homeowners here in West Michigan. Very nice people by and large.

Industry/Entity Type

Landscaping

Contact Information for Business Card

The card should be standard size with round edges maybe?

Font styles to use
Serif
Sans Serif
Decorative

Requirements
Must have
• Must haves:
• 1. Address: 4817 Larkspur Meadow Drive SE, Grand Rapids, Michigan 49546
• 2. Phone: 616.555.0187
• 3. Email: company@foxhollowgrounds.com
• 4. URL: www.foxhollowgrounds.com
• 5. Names/Titles: (1) Dennis Harlow, President (2) Mateo Vilches, Director of Field Services
Nice to have
• On the back side of the card, we are thinking it would make sense to have a short listing of services offered...
• Landscape design & installation, Professional lawn maintenance, Spring & fall leaf cleanup, Irrigation system installation & maintenance, Snowplowing, Fertilizer & weed control, Tree maintenance and removal, Landscape bed maintenance
Should not have
• Our hope is that the design won't be too ostentatious. We are looking for professional and attractive.

```html
<!DOCTYPE html>
<html lang="en">
<head>
<meta charset="utf-8">
<title>Fox Hollow Grounds – Business Cards</title>
<link rel="stylesheet" href="https://fonts.googleapis.com/css2?family=Open+Sans:wght@400;600;700;800&display=swap">
<style>
  :root {
    --backdrop: #2e2e2e;
    --card-paper: #f2f2f4;
    --leaf-green: #4cb860;
    --leaf-edge: #1f6b35;
    --ink-dark: #353b3f;
    --ink-grey: #4a4f55;
    --accent-blue: #2a7fc9;
    --name-blue: #2f86d6;
    --white: #ffffff;
  }
  * { margin: 0; padding: 0; box-sizing: border-box; }
  html, body {
    width: 1200px; height: 1000px; overflow: hidden;
    background: var(--backdrop);
    font-family: "Open Sans", Arial, sans-serif;
  }
  .card {
    position: absolute;
    left: 280px;
    width: 640px; height: 366px;
    border-radius: 30px;
    overflow: hidden;
    background: var(--card-paper);
  }
  .card--back { top: 100px; }
  .card--front { top: 534px; }
  .card svg { position: absolute; inset: 0; }

  /* back side */
  .services-tag {
    position: absolute; left: 128px; top: 96px;
    width: 150px; height: 40px;
    border: 3px solid var(--leaf-edge); border-radius: 12px;
    background: var(--card-paper);
    display: flex; align-items: center; justify-content: center;
    font-weight: 800; font-size: 19px; color: var(--ink-dark); letter-spacing: .5px;
  }
  .services-list {
    position: absolute; left: 360px; top: 68px; width: 250px;
    list-style: none; text-align: center;
    color: var(--white); font-size: 14px; line-height: 19px;
  }
  .address {
    position: absolute; left: 36px; top: 302px;
    color: var(--white); font-size: 15px; white-space: nowrap;
    transform: rotate(5deg); transform-origin: left center;
  }

  /* front side */
  .company-name {
    position: absolute; left: 110px; top: 70px; width: 500px;
    text-align: center; white-space: nowrap;
    font-weight: 600; font-size: 30px; letter-spacing: 3px;
    color: var(--ink-grey);
  }
  .person { position: absolute; left: 48px; top: 232px; }
  .person__name { color: var(--name-blue); font-weight: 800; font-size: 26px; line-height: 1.1; }
  .person__title { color: var(--white); font-size: 19px; }
  .divider {
    position: absolute; left: 272px; top: 226px;
    width: 1.5px; height: 84px; background: var(--white);
  }
  .contact {
    position: absolute; left: 296px; top: 236px;
    list-style: none; color: var(--white); font-size: 17px; line-height: 26px;
  }
  .contact li { display: flex; align-items: center; gap: 10px; }
  .contact svg { position: static; width: 17px; height: 17px; flex: none; }
</style>
</head>
<body>

<section class="card card--back" aria-label="Card back: services">
  <svg viewBox="0 0 640 366" width="640" height="366" aria-hidden="true">
    <path d="M0,230 C160,232 330,296 640,328 L640,366 L0,366 Z" fill="var(--leaf-green)"/>
    <path d="M0,230 C160,232 330,296 640,328" fill="none" stroke="var(--leaf-edge)" stroke-width="3"/>
    <line x1="0" y1="102" x2="354" y2="140" stroke="var(--leaf-edge)" stroke-width="2.5"/>
    <path d="M540,22 C606,80 634,180 590,250 C552,308 430,312 380,260 C334,206 352,110 430,64 C470,42 512,30 540,22 Z"
          fill="var(--leaf-green)" stroke="var(--leaf-edge)" stroke-width="3"/>
  </svg>
  <div class="services-tag">SERVICES</div>
  <ul class="services-list">
    <li>-Snowplowing</li>
    <li>-Fertilizer &amp; weed control</li>
    <li>-Tree maintenance and removal</li>
    <li>-Landscape bed maintenance</li>
    <li>-Landscape design &amp; installation</li>
    <li>-Professional lawn maintenance</li>
    <li>-Spring &amp; fall leaf cleanup</li>
    <li>-Irrigation system installation</li>
    <li>&amp; maintenance</li>
  </ul>
  <p class="address">4817 Larkspur Meadow Drive SE, Grand Rapids, Michigan 49546</p>
</section>

<section class="card card--front" aria-label="Card front: contact">
  <svg viewBox="0 0 640 366" width="640" height="366" aria-hidden="true">
    <path d="M0,150 C160,138 300,170 420,200 C520,224 580,214 640,196 L640,366 L0,366 Z" fill="var(--ink-dark)"/>
    <path d="M0,150 C160,138 300,170 420,200 C520,224 580,214 640,196" fill="none" stroke="var(--accent-blue)" stroke-width="6"/>
  </svg>
  <div class="company-name">FOX HOLLOW GROUNDS</div>
  <div class="person">
    <p class="person__name">Dennis Harlow</p>
    <p class="person__title">President</p>
  </div>
  <div class="divider"></div>
  <ul class="contact">
    <li>
      <svg viewBox="0 0 24 24" aria-hidden="true"><path d="M6.6 10.8a15 15 0 0 0 6.6 6.6l2.2-2.2a1 1 0 0 1 1-.25 11.4 11.4 0 0 0 3.6.57 1 1 0 0 1 1 1V20a1 1 0 0 1-1 1A17 17 0 0 1 3 4a1 1 0 0 1 1-1h3.5a1 1 0 0 1 1 1c0 1.25.2 2.45.57 3.57a1 1 0 0 1-.25 1Z" fill="var(--leaf-green)"/></svg>
      616.555.0187
    </li>
    <li>
      <svg viewBox="0 0 24 24" aria-hidden="true"><rect x="2.5" y="5" width="19" height="14" rx="1.5" fill="none" stroke="var(--leaf-green)" stroke-width="2"/><path d="M3 6l9 7 9-7" fill="none" stroke="var(--leaf-green)" stroke-width="2"/></svg>
      company@foxhollowgrounds.com
    </li>
    <li>
      <svg viewBox="0 0 24 24" aria-hidden="true"><g fill="none" stroke="var(--leaf-green)" stroke-width="1.8"><circle cx="12" cy="12" r="9.5"/><ellipse cx="12" cy="12" rx="4" ry="9.5"/><path d="M2.5 12h19M4 7h16M4 17h16"/></g></svg>
      www.foxhollowgrounds.com
    </li>
  </ul>
</section>

</body>
</html>
```